Business Card Design for new consultancy company

Name of Company: Cobalt Wayline
Nature of Business: Digital Business Consultancy
Specialises in Digital Media Strategy, Digital Business Model Transformation, Over-The-Top (OTT) Development, Web Business Development, Digital Marketing, Web and App Product Development, Design and Innovation

Website: http://www.cobalt-wayline.example

Designs can be of any colour or any number of colours, objective is to give the impression we are a digital trend setter, creative and impactful.

Also please suggest a logo to complement the name and business card.

Target Market(s)

Media Companies, Telcos, Enterprises

Industry/Entity Type

Business

Contact Information for Business Card

Standard business card size. OK with to play with small variations like corners for impact/impression.

Font styles to use
Serif
Sans Serif

Requirements
Must have
• Clarity, Impact, Creativity
Nice to have
• Design should encapsulate professionalism, expertise, yet trend-setting and vibrant for digital consultancy
Should not have
• Messy layout, too gaudy colours or design

```html
<!DOCTYPE html>
<html lang="en">
<head>
<meta charset="utf-8">
<title>Cobalt Wayline — Business Cards</title>
<link rel="stylesheet" href="https://fonts.googleapis.com/css2?family=Lato:wght@400;700&display=swap">
<style>
  :root {
    --backdrop: #2b2826;
    --card-dark: #1c1c1e;
    --card-dark-edge: #242426;
    --accent: #f04a14;
    --ink-light: #ffffff;
    --ink-muted: #e6e6e6;
    --divider: #3a3a3c;
  }
  * { box-sizing: border-box; margin: 0; padding: 0; }
  html, body {
    width: 1200px;
    height: 844px;
    overflow: hidden;
    background: var(--backdrop);
    font-family: "Lato", Arial, sans-serif;
  }
  .stage {
    position: relative;
    width: 1200px;
    height: 844px;
    display: flex;
    align-items: center;
    justify-content: center;
    gap: 50px;
  }
  .card {
    position: relative;
    width: 520px;
    height: 300px;
    overflow: hidden;
  }
  .card--back {
    background: linear-gradient(135deg, var(--card-dark-edge), var(--card-dark));
    color: var(--ink-light);
  }
  .card--front {
    background: var(--accent);
    color: var(--ink-light);
  }
  .brand {
    position: absolute;
    display: flex;
    flex-direction: column;
    align-items: center;
    gap: 16px;
  }
  .brand__dot {
    width: 54px;
    height: 54px;
    border-radius: 50%;
    border: 5px solid var(--ink-light);
  }
  .brand__name {
    font-weight: 400;
    text-transform: uppercase;
    letter-spacing: 0.02em;
    white-space: nowrap;
  }
  .card--back .brand {
    left: 30px;
    top: 96px;
    width: 210px;
  }
  .card--back .brand__name {
    color: var(--accent);
    font-size: 21px;
  }
  .divider {
    position: absolute;
    left: 258px;
    top: 40px;
    width: 1px;
    height: 220px;
    background: var(--divider);
  }
  .contact {
    position: absolute;
    left: 282px;
    top: 46px;
    right: 20px;
  }
  .contact__name {
    font-size: 24px;
    font-weight: 700;
    line-height: 1.1;
  }
  .contact__role {
    color: var(--accent);
    font-size: 13px;
    margin-top: 2px;
  }
  .contact__lines {
    list-style: none;
    margin-top: 24px;
    font-size: 13.5px;
    line-height: 1.4;
    color: var(--ink-muted);
  }
  .contact__label { color: var(--accent); margin-right: 4px; }
  .contact__address {
    margin-top: 18px;
    font-size: 13.5px;
    line-height: 1.4;
    color: var(--ink-muted);
    font-style: normal;
  }
  .card--front .brand {
    left: 0;
    right: 0;
    top: 52px;
  }
  .card--front .brand__name {
    font-size: 30px;
  }
  .services {
    position: absolute;
    left: 40px;
    right: 40px;
    top: 206px;
    text-align: center;
    font-size: 13px;
    line-height: 1.45;
    color: var(--ink-muted);
  }
</style>
</head>
<body>
  <main class="stage">
    <section class="card card--back" aria-label="Business card back with contact details">
      <div class="brand">
        <span class="brand__dot" aria-hidden="true"></span>
        <span class="brand__name">Cobalt Wayline</span>
      </div>
      <span class="divider" aria-hidden="true"></span>
      <div class="contact">
        <h1 class="contact__name">Jonah Reyes</h1>
        <p class="contact__role">Managing Director</p>
        <ul class="contact__lines">
          <li><span class="contact__label">T:</span>041-555 018 240</li>
          <li><span class="contact__label">E:</span>info@cobalt-wayline.example</li>
          <li><span class="contact__label">W:</span>www.cobalt-wayline.example</li>
        </ul>
        <address class="contact__address">12345, Address Goes Here<br>Country Name, 123456.</address>
      </div>
    </section>

    <section class="card card--front" aria-label="Business card front with company name">
      <div class="brand">
        <span class="brand__dot" aria-hidden="true"></span>
        <span class="brand__name">Cobalt Wayline</span>
      </div>
      <p class="services">Web Business Development | Digital Marketing | Web<br>and App Product Development | Design and Innovation</p>
    </section>
  </main>
</body>
</html>
```